Design of a web-based smart-home control system as part of a bachelor thesis

Within the scope of my bachelor thesis I am currently developing a central control system for the smart home. The software should be able to run mainly on a tablet (display resolution on request).

For this purpose I need a modern, user-friendly design. All graphic elements should be in SVG format, so that they can be animated eg by JavaScript, eg filling level of buffer memory.

Elements which can be connected are:
- fireplace with integrated water boiler
- e-car
- PV
- Solar thermal energy
- Buffer storage
- Smart Home elements such as heating, lighting and shutters

Currently high charts are used as diagram library.

Number of Pages Required

1 page

Font styles to use
Sans Serif

```html
<!DOCTYPE html>
<html lang="en">
<head>
<meta charset="utf-8">
<title>Homeflux – Energy Dashboard</title>
<link rel="stylesheet" href="https://fonts.googleapis.com/css2?family=Roboto:wght@300;400;500&display=swap">
<style>
  :root {
    --page-bg: #263044;
    --header-bg: #232b3e;
    --panel-bg: #2d384f;
    --dock-bg: #1c2333;
    --dock-active: #263044;
    --text-strong: #ffffff;
    --text-label: #a7b3c8;
    --text-muted: #7f8ba0;
    --grid-line: #222b3d;
    --divider: #3a4660;
    --icon: #8c97aa;
    --yellow: #f2c14e;
    --red: #e8453c;
    --green: #17c28e;
    --badge: #1e90ff;
  }
  * { box-sizing: border-box; margin: 0; padding: 0; }
  html, body { width: 1200px; height: 900px; overflow: hidden; }
  body {
    background: var(--page-bg);
    font-family: "Roboto", sans-serif;
    color: var(--text-strong);
    position: relative;
  }
  .top-bar {
    position: absolute; left: 0; top: 0; width: 1200px; height: 63px;
    background: var(--header-bg);
    border-bottom: 1px solid #20283a;
  }
  .brand {
    position: absolute; left: 29px; top: 17px;
    font-size: 25px; font-weight: 400; letter-spacing: 0.3px;
    display: flex; align-items: center; gap: 7px;
  }
  .brand-dot { width: 8px; height: 8px; border-radius: 50%; background: var(--text-strong); }
  .bar-divider { position: absolute; top: 0; width: 1px; height: 63px; background: #1f2738; }
  .menu-toggle { position: absolute; left: 238px; top: 28px; }
  .top-actions { position: absolute; right: 0; top: 0; height: 63px; }
  .top-icon { position: absolute; top: 21px; }
  .user-menu {
    position: absolute; left: 1087px; top: 21px; font-size: 15px; color: #dfe5ef;
    display: flex; align-items: center; gap: 10px; white-space: nowrap;
  }

  .panel { position: absolute; left: 30px; width: 1140px; background: var(--panel-bg); }
  .stats { top: 81px; height: 113px; }
  .stat { position: absolute; top: 28px; }
  .stat-label { font-size: 12px; font-weight: 500; color: var(--text-label); letter-spacing: 0.6px; }
  .stat-value { display: flex; align-items: flex-start; margin-top: 6px; }
  .stat-number { font-size: 39px; font-weight: 300; line-height: 44px; }
  .stat-unit {
    margin-left: 9px; margin-top: 5px; font-size: 9px; font-weight: 500; color: var(--text-label);
    display: flex; flex-direction: column; align-items: center; gap: 5px;
  }
  .stat-divider { position: absolute; top: 47px; width: 1px; height: 40px; background: var(--divider); }

  .section-title {
    position: absolute; left: 33px; font-size: 19px; font-weight: 500;
    color: var(--text-label); letter-spacing: 0.8px;
  }
  .chart-panel { top: 212px; height: 385px; }
  .chart { position: absolute; left: 0; top: 0; }
  .legend {
    position: absolute; top: 349px; left: 0; font-size: 10px; font-weight: 500; color: var(--text-label);
  }
  .legend-item { position: absolute; display: flex; align-items: center; gap: 6px; white-space: nowrap; }
  .legend-dot { width: 7px; height: 7px; border-radius: 50%; }

  .tech-panel { top: 616px; height: 156px; }
  .tech-item { position: absolute; top: 76px; }
  .tech-label {
    font-size: 12px; font-weight: 500; color: var(--text-label); letter-spacing: 0.6px; line-height: 18px;
  }
  .tech-gauge {
    position: absolute; width: 67px; height: 67px; border-radius: 50%;
    border: 1.5px solid #7a869b; background: #243046;
    display: flex; align-items: center; justify-content: center;
    font-size: 16px; font-weight: 300; color: var(--text-strong);
  }

  .device-dock { position: absolute; left: 0; top: 791px; width: 1200px; height: 109px; background: var(--dock-bg); }
  .dock-active { position: absolute; left: 33px; top: 0; width: 111px; height: 109px; background: var(--dock-active); }
  .dock-icon { position: absolute; top: 21px; width: 60px; height: 60px; }
  .dock-sep { position: absolute; top: 41px; width: 1px; height: 41px; background: #3a4560; }
</style>
</head>
<body>

<header class="top-bar">
  <div class="brand"><span class="brand-dot"></span>Homeflux</div>
  <div class="bar-divider" style="left:213px"></div>
  <div class="bar-divider" style="left:285px"></div>
  <svg class="menu-toggle" width="21" height="14" viewBox="0 0 21 14" aria-label="Menu">
    <g stroke="#8c97aa" stroke-width="2"><line x1="0" y1="1" x2="21" y2="1"/><line x1="0" y1="7" x2="21" y2="7"/><line x1="0" y1="13" x2="21" y2="13"/></g>
  </svg>
  <svg class="top-icon" style="left:962px" width="19" height="19" viewBox="0 0 20 20" aria-label="Help">
    <circle cx="10" cy="10" r="9.5" fill="#8c97aa"/>
    <path d="M7.3 7.6a2.8 2.8 0 1 1 3.9 2.6c-.9.4-1.2.9-1.2 1.9" fill="none" stroke="#232b3e" stroke-width="2"/>
    <circle cx="10" cy="15" r="1.2" fill="#232b3e"/>
  </svg>
  <svg class="top-icon" style="left:1004px;top:24px" width="19" height="14" viewBox="0 0 19 14" aria-label="Messages">
    <rect width="19" height="14" rx="1.5" fill="#8c97aa"/>
    <path d="M1 1.5l8.5 6 8.5-6" fill="none" stroke="#232b3e" stroke-width="1.6"/>
  </svg>
  <svg class="top-icon" style="left:1045px" width="20" height="20" viewBox="0 0 20 20" aria-label="Notifications">
    <path d="M9 2.5a5 5 0 0 0-5 5v5l-2 2.5h14l-2-2.5v-5a5 5 0 0 0-5-5z" fill="#8c97aa"/>
    <path d="M7.5 16.5a1.6 1.6 0 0 0 3 0z" fill="#8c97aa"/>
    <circle cx="14.5" cy="3.5" r="3.5" fill="var(--badge)"/>
  </svg>
  <div class="user-menu">Username
    <svg width="9" height="5" viewBox="0 0 9 5"><path d="M0 0h9L4.5 5z" fill="#8c97aa"/></svg>
  </div>
</header>

<section class="panel stats">
  <div class="stat" style="left:36px">
    <div class="stat-label">POWER AT GRID CONNECTION POINT</div>
    <div class="stat-value"><span class="stat-number">583</span><span class="stat-unit">W<span>↑</span></span></div>
  </div>
  <div class="stat-divider" style="left:273px"></div>
  <div class="stat" style="left:314px">
    <div class="stat-label">PV POWER</div>
    <div class="stat-value"><span class="stat-number">1364</span><span class="stat-unit">W<span>↑</span></span></div>
  </div>
  <div class="stat-divider" style="left:552px"></div>
  <div class="stat" style="left:596px">
    <div class="stat-label">GRID REFERENCE</div>
    <div class="stat-value"><span class="stat-number">5.048</span><span class="stat-unit">KWH<span>↑</span></span></div>
  </div>
  <div class="stat-divider" style="left:834px"></div>
  <div class="stat" style="left:878px">
    <div class="stat-label">DAILY YIELD</div>
    <div class="stat-value"><span class="stat-number">4.512</span><span class="stat-unit">KWH<span>↑</span></span></div>
  </div>
</section>

<section class="panel chart-panel">
  <h2 class="section-title" style="top:26px">DAILY PROGRESSIONS</h2>
  <svg class="chart" width="1140" height="385" viewBox="51 362 1945 657" aria-label="Daily power progression chart">
    <defs>
      <linearGradient id="self-fill" x1="0" y1="0" x2="0" y2="1">
        <stop offset="0" stop-color="#17c28e" stop-opacity="0.28"/>
        <stop offset="1" stop-color="#17c28e" stop-opacity="0"/>
      </linearGradient>
    </defs>
    <g stroke="var(--grid-line)" stroke-width="1.6">
      <line x1="178" y1="517" x2="1916" y2="517"/><line x1="178" y1="599" x2="1916" y2="599"/>
      <line x1="178" y1="681" x2="1916" y2="681"/><line x1="178" y1="763" x2="1916" y2="763"/>
      <line x1="178" y1="847" x2="1916" y2="847"/>
      <line x1="178" y1="517" x2="178" y2="847"/><line x1="258" y1="517" x2="258" y2="847"/>
      <line x1="335" y1="517" x2="335" y2="847"/><line x1="415" y1="517" x2="415" y2="847"/>
      <line x1="495" y1="517" x2="495" y2="847"/><line x1="575" y1="517" x2="575" y2="847"/>
      <line x1="652" y1="517" x2="652" y2="847"/><line x1="732" y1="517" x2="732" y2="847"/>
      <line x1="810" y1="517" x2="810" y2="847"/><line x1="890" y1="517" x2="890" y2="847"/>
      <line x1="967" y1="517" x2="967" y2="847"/><line x1="1047" y1="517" x2="1047" y2="847"/>
      <line x1="1127" y1="517" x2="1127" y2="847"/><line x1="1207" y1="517" x2="1207" y2="847"/>
      <line x1="1285" y1="517" x2="1285" y2="847"/><line x1="1365" y1="517" x2="1365" y2="847"/>
      <line x1="1442" y1="517" x2="1442" y2="847"/><line x1="1522" y1="517" x2="1522" y2="847"/>
      <line x1="1600" y1="517" x2="1600" y2="847"/><line x1="1680" y1="517" x2="1680" y2="847"/>
      <line x1="1758" y1="517" x2="1758" y2="847"/><line x1="1838" y1="517" x2="1838" y2="847"/>
      <line x1="1916" y1="517" x2="1916" y2="847"/>
    </g>
    <g font-family="Roboto, sans-serif" font-size="19" fill="var(--text-muted)" text-anchor="end">
      <text x="150" y="524">6k</text><text x="150" y="606">4k</text><text x="150" y="688">3k</text>
      <text x="150" y="770">2k</text><text x="150" y="853">0</text>
    </g>
    <g font-family="Roboto, sans-serif" font-size="16" fill="var(--text-muted)" text-anchor="middle">
      <text x="187" y="909">DEC</text><text x="258" y="909">01.00</text><text x="337" y="909">02.00</text>
      <text x="416" y="909">03.00</text><text x="495" y="909">04.00</text><text x="573" y="909">05.00</text>
      <text x="651" y="909">06.00</text><text x="732" y="909">07.00</text><text x="808" y="909">08.00</text>
      <text x="889" y="909">09.00</text><text x="967" y="909">10.00</text><text x="1045" y="909">11.00</text>
      <text x="1125" y="909">12.00</text><text x="1204" y="909">13.00</text><text x="1285" y="909">14.00</text>
      <text x="1366" y="909">15.00</text><text x="1439" y="909">16.00</text><text x="1523" y="909">17.00</text>
      <text x="1598" y="909">18.00</text><text x="1680" y="909">19.00</text><text x="1761" y="909">20.00</text>
      <text x="1839" y="909">21.00</text><text x="1915" y="909">22.00</text>
    </g>
    <polygon fill="url(#self-fill)" points="178,851 335,711 495,595 652,563 810,599 967,680 1127,692 1285,612 1442,723 1600,669 1758,668 1916,680 1916,847 178,847"/>
    <g fill="none" stroke-width="2">
      <polyline stroke="var(--green)" points="178,851 335,711 495,595 652,563 810,599 967,680 1127,692 1285,612 1442,723 1600,669 1758,668 1916,680"/>
      <polyline stroke="var(--yellow)" points="178,851 335,672 495,648 652,672 810,654 967,672 1127,636 1285,648 1442,630 1600,636 1758,701 1916,637"/>
      <polyline stroke="var(--red)" points="178,851 335,748 495,711 652,723 810,711 967,738 1127,711 1285,710 1442,674 1600,723 1758,747 1916,731"/>
    </g>
    <g fill="var(--panel-bg)" stroke-width="1.5">
      <g stroke="var(--green)">
        <circle cx="335" cy="711" r="3"/><circle cx="495" cy="595" r="3"/><circle cx="652" cy="563" r="3"/><circle cx="810" cy="599" r="3"/>
        <circle cx="967" cy="680" r="3"/><circle cx="1127" cy="692" r="3"/><circle cx="1285" cy="612" r="3"/><circle cx="1442" cy="723" r="3"/>
        <circle cx="1600" cy="669" r="3"/><circle cx="1758" cy="668" r="3"/><circle cx="1916" cy="680" r="3"/>
      </g>
      <g stroke="var(--yellow)">
        <circle cx="335" cy="672" r="3"/><circle cx="495" cy="648" r="3"/><circle cx="652" cy="672" r="3"/><circle cx="810" cy="654" r="3"/>
        <circle cx="967" cy="672" r="3"/><circle cx="1127" cy="636" r="3"/><circle cx="1285" cy="648" r="3"/><circle cx="1442" cy="630" r="3"/>
        <circle cx="1600" cy="636" r="3"/><circle cx="1758" cy="701" r="3"/><circle cx="1916" cy="637" r="3"/>
      </g>
      <g stroke="var(--red)">
        <circle cx="335" cy="748" r="3"/><circle cx="495" cy="711" r="3"/><circle cx="652" cy="723" r="3"/><circle cx="810" cy="711" r="3"/>
        <circle cx="967" cy="738" r="3"/><circle cx="1127" cy="711" r="3"/><circle cx="1285" cy="710" r="3"/><circle cx="1442" cy="674" r="3"/>
        <circle cx="1600" cy="723" r="3"/><circle cx="1758" cy="747" r="3"/><circle cx="1916" cy="731" r="3"/>
      </g>
    </g>
  </svg>
  <div class="legend">
    <span class="legend-item" style="left:421px"><span class="legend-dot" style="background:var(--yellow)"></span>Output power</span>
    <span class="legend-item" style="left:539px"><span class="legend-dot" style="background:var(--red)"></span>Grid reference</span>
    <span class="legend-item" style="left:664px"><span class="legend-dot" style="background:var(--green)"></span>Self using</span>
  </div>
</section>

<section class="panel tech-panel">
  <h2 class="section-title" style="top:20px">TECHNICAL DATA</h2>
  <div class="tech-item" style="left:36px"><div class="tech-label">POWER STRING 1<br>(EAST-SIDE)</div></div>
  <div class="tech-gauge" style="left:158px;top:49px">557</div>
  <div class="tech-item" style="left:286px"><div class="tech-label">POWER STRING 2<br>(WEST-SIDE)</div></div>
  <div class="tech-gauge" style="left:408px;top:49px">807</div>
  <div class="tech-item" style="left:543px"><div class="tech-label">VOLTAGE STRING 1<br>(EAST-SIDE)</div></div>
  <div class="tech-gauge" style="left:665px;top:49px">486.3</div>
  <div class="tech-item" style="left:793px"><div class="tech-label">VOLTAGE STRING 2<br>(WEST-SIDE)</div></div>
  <div class="tech-gauge" style="left:915px;top:49px">545.57</div>
</section>

<nav class="device-dock" aria-label="Connected devices">
  <div class="dock-active"></div>
  <svg class="dock-icon" style="left:58px" viewBox="0 0 60 60" fill="none" stroke="var(--icon)" stroke-width="2.4" aria-label="Photovoltaics">
    <path d="M22 22a8 8 0 0 1 16 0"/><line x1="30" y1="4" x2="30" y2="9"/><line x1="17" y1="10" x2="20" y2="13"/><line x1="43" y1="10" x2="40" y2="13"/>
    <path d="M12 24h36l4 20H8z"/><line x1="10" y1="31" x2="50" y2="31"/><line x1="9" y1="38" x2="51" y2="38"/>
    <line x1="21" y1="24" x2="19" y2="44"/><line x1="30" y1="24" x2="30" y2="44"/><line x1="39" y1="24" x2="41" y2="44"/>
    <line x1="30" y1="44" x2="30" y2="54"/><line x1="20" y1="55" x2="40" y2="55"/>
  </svg>
  <svg class="dock-icon" style="left:176px" viewBox="0 0 60 60" fill="none" stroke="var(--icon)" stroke-width="2.4" aria-label="Fireplace with water boiler">
    <rect x="2" y="4" width="56" height="6"/><rect x="4" y="10" width="52" height="44"/><rect x="2" y="54" width="56" height="4"/>
    <path d="M14 54V24l16-8 16 8v30"/>
    <path d="M30 30c-1 6-8 9-8 16a8 8 0 0 0 16 0c0-5-4-6-4-10-2 3-3 4-4 4 1-4 0-7 0-10z"/>
  </svg>
  <svg class="dock-icon" style="left:303px" viewBox="0 0 60 60" fill="none" stroke="var(--icon)" stroke-width="2.4" aria-label="Electric car">
    <path d="M14 18h8M38 18h8"/><path d="M10 32l4-14M50 32l-4-14"/><rect x="4" y="32" width="52" height="18" rx="3"/>
    <circle cx="14" cy="41" r="3"/><circle cx="46" cy="41" r="3"/><path d="M10 50v5h8v-5M42 50v5h8v-5"/>
    <path d="M32 4l-6 14h6l-4 12 10-16h-6l4-10z" fill="var(--icon)"/>
  </svg>
  <svg class="dock-icon" style="left:426px" viewBox="0 0 60 60" fill="none" stroke="var(--icon)" stroke-width="2.4" aria-label="Buffer storage">
    <ellipse cx="30" cy="9" rx="26" ry="6"/><path d="M4 9v42c0 3.3 11.6 6 26 6s26-2.7 26-6V9"/>
    <path d="M4 23c0 3.3 11.6 6 26 6s26-2.7 26-6M4 37c0 3.3 11.6 6 26 6s26-2.7 26-6"/>
  </svg>
  <svg class="dock-icon" style="left:547px" viewBox="0 0 60 60" fill="none" stroke="var(--icon)" stroke-width="2.4" aria-label="Heating">
    <path d="M14 38V8a5 5 0 0 1 10 0v30a9 9 0 1 1-10 0z"/><circle cx="19" cy="46" r="3"/><line x1="19" y1="20" x2="19" y2="43"/>
    <circle cx="42" cy="20" r="7"/>
    <g stroke-width="3"><line x1="42" y1="7" x2="42" y2="10"/><line x1="42" y1="30" x2="42" y2="33"/><line x1="29" y1="20" x2="32" y2="20"/><line x1="52" y1="20" x2="55" y2="20"/>
    <line x1="33" y1="11" x2="35" y2="13"/><line x1="49" y1="27" x2="51" y2="29"/><line x1="51" y1="11" x2="49" y2="13"/><line x1="35" y1="27" x2="33" y2="29"/></g>
  </svg>
  <svg class="dock-icon" style="left:661px" viewBox="0 0 60 60" fill="none" stroke="var(--icon)" stroke-width="2.4" aria-label="Lighting">
    <path d="M22 42c0-6-8-10-8-20a16 16 0 0 1 32 0c0 10-8 14-8 20z"/><path d="M22 47h16M23 52h14"/><path d="M27 56h6"/>
    <line x1="4" y1="22" x2="8" y2="22"/><line x1="52" y1="22" x2="56" y2="22"/><line x1="6" y1="10" x2="9" y2="12"/><line x1="54" y1="10" x2="51" y2="12"/>
    <line x1="6" y1="34" x2="9" y2="32"/><line x1="54" y1="34" x2="51" y2="32"/>
  </svg>
  <svg class="dock-icon" style="left:779px" viewBox="0 0 60 60" fill="none" stroke="var(--icon)" stroke-width="2.4" aria-label="Shutters">
    <path d="M6 6h46M10 6v48h36V6"/><circle cx="52" cy="8" r="3"/>
    <line x1="10" y1="14" x2="46" y2="14"/><line x1="10" y1="20" x2="46" y2="20"/><line x1="10" y1="26" x2="46" y2="26"/>
    <line x1="10" y1="32" x2="46" y2="32"/><line x1="10" y1="38" x2="46" y2="38"/><line x1="10" y1="44" x2="46" y2="44"/>
  </svg>
  <div class="dock-sep" style="left:271px"></div>
  <div class="dock-sep" style="left:395px"></div>
  <div class="dock-sep" style="left:518px"></div>
  <div class="dock-sep" style="left:636px"></div>
  <div class="dock-sep" style="left:749px"></div>
  <div class="dock-sep" style="left:865px"></div>
</nav>

</body>
</html>
```